Business card design needed

Bright Path Ahead is an online wellness program designed for people dealing with cancer to take control of their lives and bright path ahead.

Target Market(s)

initially woman aged 35 to 65 years eventaully then men

Industry/Entity Type

Business

Contact Information for Business Card

Marlena Throsby
Bright path ahead Coach
Marlena@brightpathway.com.au
M 0418392716
Skype Marlena.Throsby
local number to come
www.brightpathway.com.au

Requirements
Must have
• Business cards want to have a photo of me on the back this is a head shot. Also a small blurb " Marlena recovered and survived 2 types of cancer. She under went a transformational 12 month journey to overcome cancer naturally . Join her online coaching program to bright path ahead.

Phone number and email and skype address.
Nice to have
• Looking for something that resembles health EG abstract tree of life, or something resembling health and balance . Like lime green/apple green want modern fresh. Want only 2 colours used on the cards. Need to use the logo and Bright path ahead on website and email signature - Clean and fresh

Also would like Letter head and logo for website and email signature

```html
<!DOCTYPE html>
<html lang="en">
<head>
<meta charset="utf-8">
<title>Marlena Throsby – Business Card</title>
<link rel="stylesheet" href="https://fonts.googleapis.com/css2?family=Quicksand:wght@500;600;700&display=swap">
<style>
  :root {
    --page: #f6f6f6;
    --card: #f2f5ec;
    --teal: #00a1b5;
    --bark: #6b5245;
    --muted: #b8b8b8;
    --white: #ffffff;
  }
  * { margin: 0; padding: 0; box-sizing: border-box; }
  html, body {
    width: 1200px; height: 636px; overflow: hidden;
    background: var(--page);
    font-family: "Quicksand", sans-serif;
  }
  .stage { position: relative; width: 1200px; height: 636px; }
  .card {
    position: absolute; top: 114px;
    width: 558px; height: 303px;
    background: var(--card);
    overflow: hidden;
  }
  .card--colour { left: 18px; }
  .card--mono { left: 622px; }
  .tree-art {
    position: absolute; left: 0; top: 12px;
    width: 172px; height: 291px;
    background: linear-gradient(180deg, var(--teal) 0%, var(--teal) 55%, var(--bark) 100%);
    opacity: .9;
    border-radius: 0 60px 0 0;
  }
  .name {
    position: absolute; left: 237px; top: 40px;
    font-size: 37px; font-weight: 600; letter-spacing: 1.5px;
    color: var(--teal); white-space: nowrap;
  }
  .role {
    position: absolute; left: 237px; top: 84px;
    font-size: 19px; font-weight: 600; letter-spacing: .6px;
    color: var(--bark);
  }
  .contacts { position: absolute; left: 238px; top: 122px; list-style: none; }
  .contact {
    display: flex; align-items: center; gap: 6px;
    height: 24px; margin-bottom: 6.5px;
    font-size: 16px; font-weight: 700; letter-spacing: .5px;
    color: var(--bark); white-space: nowrap;
  }
  .contact-icon { width: 24px; height: 24px; flex: none; }
  .contact-icon circle { fill: var(--teal); }
  .card--mono .contact-icon circle { fill: var(--muted); }
  .web-band {
    position: absolute; left: 238px; top: 263px;
    width: 320px; height: 25px;
    background: var(--teal); color: var(--white);
    font-size: 19px; font-weight: 600; letter-spacing: 1.6px;
    line-height: 25px; padding-left: 9px;
  }
</style>
</head>
<body>
<main class="stage">

  <section class="card card--colour">
    <div class="tree-art" role="img" aria-label="Abstract tree of life with brown trunk and teal leaves"></div>
    <h1 class="name">Marlena Throsby</h1>
    <p class="role">Bright path ahead Coach</p>
    <ul class="contacts">
      <li class="contact">
        <svg class="contact-icon" viewBox="0 0 24 24"><circle cx="12" cy="12" r="12"/><rect x="8.5" y="5" width="7" height="14" rx="1.5" fill="none" stroke="#fff" stroke-width="1.4"/><circle cx="12" cy="16.5" r=".9" style="fill:#fff"/></svg>
        M 0418392716
      </li>
      <li class="contact">
        <svg class="contact-icon" viewBox="0 0 24 24"><circle cx="12" cy="12" r="12"/><rect x="5.5" y="7.5" width="13" height="9" fill="none" stroke="#fff" stroke-width="1.4"/><path d="M5.5 7.5 12 13l6.5-5.5" fill="none" stroke="#fff" stroke-width="1.4"/></svg>
        Marlena@brightpathway.com.au
      </li>
      <li class="contact">
        <svg class="contact-icon" viewBox="0 0 24 24"><circle cx="12" cy="12" r="12"/></svg>
        Marlena.Throsby
      </li>
      <li class="contact">
        <svg class="contact-icon" viewBox="0 0 24 24"><circle cx="12" cy="12" r="12"/><path d="M8 6c-1.5 1-2 3 0 6.5S13.5 19 15.5 18l1.5-1.5-2.5-2.5-1.5 1c-1-.5-2.5-2.5-3-3.5l1-1.5L8.5 5.5Z" fill="#fff"/></svg>
        Local number to come
      </li>
    </ul>
    <div class="web-band">www.brightpathway.com.au</div>
  </section>

  <section class="card card--mono">
    <div class="tree-art" role="img" aria-label="Abstract tree of life with brown trunk and teal leaves"></div>
    <h1 class="name">Marlena Throsby</h1>
    <p class="role">Bright path ahead Coach</p>
    <ul class="contacts">
      <li class="contact">
        <svg class="contact-icon" viewBox="0 0 24 24"><circle cx="12" cy="12" r="12"/><rect x="8.5" y="5" width="7" height="14" rx="1.5" fill="none" stroke="#fff" stroke-width="1.4"/><circle cx="12" cy="16.5" r=".9" style="fill:#fff"/></svg>
        M 0418392716
      </li>
      <li class="contact">
        <svg class="contact-icon" viewBox="0 0 24 24"><circle cx="12" cy="12" r="12"/><rect x="5.5" y="7.5" width="13" height="9" fill="none" stroke="#fff" stroke-width="1.4"/><path d="M5.5 7.5 12 13l6.5-5.5" fill="none" stroke="#fff" stroke-width="1.4"/></svg>
        Marlena@brightpathway.com.au
      </li>
      <li class="contact">
        <svg class="contact-icon" viewBox="0 0 24 24"><circle cx="12" cy="12" r="12"/></svg>
        Marlena.Throsby
      </li>
      <li class="contact">
        <svg class="contact-icon" viewBox="0 0 24 24"><circle cx="12" cy="12" r="12"/><path d="M8 6c-1.5 1-2 3 0 6.5S13.5 19 15.5 18l1.5-1.5-2.5-2.5-1.5 1c-1-.5-2.5-2.5-3-3.5l1-1.5L8.5 5.5Z" fill="#fff"/></svg>
        Local number to come
      </li>
    </ul>
    <div class="web-band">www.brightpathway.com.au</div>
  </section>

</main>
</body>
</html>
```